Ironleaf Foundry Business cards

been in business since 1982
do lost wax casting
primary products are police, fire, QRV ect. badges
custom belt buckles, money clips, coins, awards

Target Market(s)

Police, fire, clubs, ect

Industry/Entity Type

Business

Contact Information for Business Card

I want them to blow your socks off

Requirements
Must have
• "our quality is your pride" Logo
Nice to have
• I have a logo but would like it tweaked
• could be 2 sided with smaller pics of our products on the back, uploading more pics.
• check my wbsite for ideas
• ironleafbuckles.example
• I had the Logo redone but am not 100% sure it exacyly the way I want it to look

```html
<!DOCTYPE html>
<html lang="en">
<head>
<meta charset="utf-8">
<title>Ironleaf Foundry – Business Cards</title>
<link rel="stylesheet" href="https://fonts.googleapis.com/css2?family=Questrial&family=Alfa+Slab+One&display=swap">
<style>
  :root {
    --stage: #3a3040;
    --card-black: #050505;
    --card-white: #ffffff;
    --bronze-dark: #5a3510;
    --bronze-mid: #b7793a;
    --bronze-light: #f3d29a;
    --ember: #f0a020;
    --ember-deep: #8a1e08;
    --text-light: #f2f2f2;
    --label-ink: #111111;
    --gold-a: #e8c872;
    --gold-b: #8a6424;
    --silver-a: #e4e4e4;
    --silver-b: #7d7d7d;
  }
  * { box-sizing: border-box; margin: 0; padding: 0; }
  html, body { width: 1200px; height: 800px; overflow: hidden; }
  body {
    background: var(--stage);
    display: flex;
    align-items: center;
    justify-content: center;
    gap: 40px;
    font-family: "Questrial", sans-serif;
  }
  .card {
    position: relative;
    width: 560px;
    height: 320px;
    overflow: hidden;
    box-shadow: 0 10px 30px rgba(0,0,0,.45);
  }
  .bronze-band {
    position: absolute;
    left: 0; right: 0;
    background: linear-gradient(90deg, var(--bronze-dark), var(--bronze-mid) 30%, var(--bronze-light) 55%, var(--bronze-mid) 75%, var(--bronze-dark));
  }
  /* Front */
  .card-front { background: var(--card-black); }
  .card-front .bronze-band { height: 24px; }
  .card-front .band-top { top: 0; }
  .card-front .band-bottom { bottom: 0; }
  .brand {
    position: absolute;
    left: 34px; top: 38px;
    display: flex; align-items: center; gap: 12px;
  }
  .brand-dot {
    width: 22px; height: 22px; border-radius: 50%;
    background: var(--ember);
    flex: none;
  }
  .brand-name {
    font-family: "Alfa Slab One", serif;
    font-size: 30px;
    line-height: 32px;
    color: var(--ember);
  }
  .contact {
    position: absolute;
    left: 34px; top: 122px;
    list-style: none;
    color: var(--text-light);
    font-size: 14px;
    line-height: 22px;
  }
  .person-name {
    position: absolute;
    right: 26px; top: 104px;
    color: var(--ember);
    font-size: 21px;
    font-weight: 700;
  }
  .pour-photo {
    position: absolute;
    left: 300px; top: 138px;
    width: 240px; height: 158px;
    background: radial-gradient(ellipse at 45% 55%, #ffe08a 0%, var(--ember) 20%, #c23a10 45%, var(--ember-deep) 70%, var(--card-black) 100%);
  }
  /* Back */
  .card-back { background: var(--card-white); }
  .card-back .bronze-band { height: 12px; }
  .card-back .band-top { top: 0; }
  .card-back .band-bottom { bottom: 0; }
  .product { position: absolute; text-align: center; }
  .product-pic { margin: 0 auto; }
  .pic-gold { background: radial-gradient(circle at 35% 30%, var(--gold-a), var(--gold-b)); }
  .pic-silver { background: radial-gradient(circle at 35% 30%, var(--silver-a), var(--silver-b)); }
  .product-label {
    display: block;
    margin-top: 6px;
    font-family: "Alfa Slab One", serif;
    font-size: 13px;
    color: var(--label-ink);
    white-space: nowrap;
  }
</style>
</head>
<body>

<section class="card card-front" aria-label="Business card front">
  <div class="bronze-band band-top"></div>
  <div class="brand">
    <span class="brand-dot"></span>
    <span class="brand-name">Ironleaf<br>Foundry</span>
  </div>
  <ul class="contact">
    <li>462 W. Cedar Ridge Rd. Marlow, TX</li>
    <li>Toll Free: 800-555-0142</li>
    <li>Cell: 214 555-0187</li>
    <li>Fax: 903-555-0163</li>
    <li>www.ironleaffoundry.example</li>
    <li>dale@ironleaffoundry.example</li>
  </ul>
  <div class="pour-photo" role="img" aria-label="Photo of molten metal pouring from a glowing crucible"></div>
  <p class="person-name">Dale Hartwell</p>
  <div class="bronze-band band-bottom"></div>
</section>

<section class="card card-back" aria-label="Business card back with products">
  <div class="bronze-band band-top"></div>

  <div class="product" style="left:34px; top:30px; width:110px;">
    <div class="product-pic pic-silver" role="img" aria-label="Photo of a rectangular stock belt buckle" style="width:96px; height:60px; border-radius:8px;"></div>
    <span class="product-label">Stock Buckles</span>
  </div>

  <div class="product" style="left:160px; top:66px; width:110px;">
    <div class="product-pic pic-gold" role="img" aria-label="Photo of a gold shield-shaped pendant" style="width:62px; height:70px; border-radius:10px 10px 30px 30px;"></div>
    <span class="product-label">Misc Products</span>
  </div>

  <div class="product" style="left:290px; top:46px; width:100px;">
    <div class="product-pic pic-silver" role="img" aria-label="Photo of a colored challenge coin" style="width:92px; height:92px; border-radius:50%;"></div>
    <span class="product-label">Coins</span>
  </div>

  <div class="product" style="left:34px; top:132px; width:100px;">
    <div class="product-pic pic-silver" role="img" aria-label="Photo of a firefighters class ring" style="width:76px; height:62px; border-radius:14px;"></div>
    <span class="product-label">Rings</span>
  </div>

  <div class="product" style="left:150px; top:172px; width:110px;">
    <div class="product-pic pic-gold" role="img" aria-label="Photo of an anniversary lapel pin" style="width:84px; height:84px; border-radius:50%;"></div>
    <span class="product-label">Lapel Pins</span>
  </div>

  <div class="product" style="left:440px; top:110px; width:100px;">
    <div class="product-pic pic-silver" role="img" aria-label="Photo of a sheriff badge" style="width:64px; height:80px; border-radius:24px 24px 32px 32px;"></div>
    <span class="product-label">Badges</span>
  </div>

  <div class="product" style="left:300px; top:190px; width:120px;">
    <div class="product-pic pic-silver" role="img" aria-label="Photo of an engraved oval trophy buckle" style="width:110px; height:76px; border-radius:50%;"></div>
    <span class="product-label">Buckles</span>
  </div>

  <div class="bronze-band band-bottom"></div>
</section>

</body>
</html>
```